Lunar Ledger - Minimalistic Single Page Web Design

Project: We are in the process of creating a new Corp Identity. Design a website for our company incorporating the Logo recently designed and selected from a SketchHive contest. (attached)

Designers: For this project, you need to design a minimalistic single page, modern website. Beside text and image placement, you will also need to describe user interface, how content is presented and so on.
- Design Layout
- Design Image placements (if any)
- Design menu and buttons
- Design menu and buttons placements
- Design content layout
- Design overall effect and feel of website
- Design color scheme
- Design content style (tone and style of content, words type, how much)
- Design user interface (how do you scroll, what happens when you mouseover buttons, where do certain links and buttons lead you)

Coding Requirements: You need to design the website with a modern perspective on website visuals and effects. Jquery, HTML5 (no FLASH please). You do not need to code for this particular contest, but if you can also code, great, tell me and let me know how I can hire you to complete it. If you know someone that can code your vision, great, let me know. If not, you need to be clear and concise, and be willing to help me communicate with a developer to get the site executed. The web site needs to be modern and dynamic.

Company Name:
Lunar Ledger; Lunar-Ledger; LunarLedger

Domain: www.lunar-ledger.example

Company Industry:
Lunar Ledger provides consulting in areas of finance, accounting, business organization, and set up.
- Bookkeeping
- Project Management
- Budget Management
- Cash Management
- Receipt Management
- Filing and Records Management
- Training of administration and accounting staff
- Financial Reports
- Spreadsheets
- Graphs, charts and trend analysis
- Business set up
- Tax filings
- Payroll and HR

Clients:
- Small to medium size businesses
- Proprietors
- Entrepreneurs
- Mom & Pops Shops
- We cater to every industry

Corporate Identity:
- Past: I have never complete a webpage for my company. I did scratch several projects that were started and never completed. I fell in love with stick figures, whimsical designs, similar to that of "Cratebin", I believed in simplicity and minimalism. However, I was not effective in find the right people to complete my project. Bits and pieces of the website was designed, but never executed.

- Current: I need a webpage design. The web design must align with the current logo aesthetics.The current logo is new. I selected this logo for its simplicity and modern feel. It also incorporated an image of a trending graph, which fits with my company's profile. Still, I am leaning towards simple design, minimalism with boldness. I like my new webpage to be mature and professional, but I want it to portray energy and youth. So no "traditional corp" like design. I like new HTML5 elements, jquery and fun and beautiful forms and buttons. Less image is more.

Note: Please improvise according to your taste and professional perspective, you do not have to follow my suggestions word for word.

Features & Layout:
- Single page layout
- Vertical scroll
- Framed sections so that it looks good on the screen
- Well designed and strategically placed menu bar
- Fills a modern browser
- Beautiful color scheme that pops
- Incorporate Logo aesthetics

Fonts and Type:
- This is an element of the overall design
- I love clean fonts
- Fonts that adds meaning to the overall effect
- Clean

Sounds
- Please no cheesy sounds and background music

Images:
- To your liking
- But please, no lame corp people in suits
- No lame photographs
- I like stick figures
- I like whimsical illustrations

Landing Page:
- This should be the bulk of your design
- The landing page must be impressive, eye catchy
- Bold

Menu Bar:
- Header (introduction and landing page)
- Service & Products
- Company (about us)
- Affiliates and Clients (reference area)
- Contact (contact us area)
- Footer

Colors:
- Up to you, I just like things clean and easy to read
- No black background behind text
- Incorporate Logo Colors

Web Effects:
- According to your liking
- You will need to be involve to communicate the layout and design to the developer, so you need to be clear in your design.

Content:
- You personally don't have to come up with the content, but if you can great.
- I will help come up with the content throughout the contect timeframe, just let me know what you want
- I do not like too much content in my website. The most for each section is 2-3 lines if any.
- Combination could also be one liners.
- I like minimalistic approach.
- If you are not creating the final content, you need to show what type of content need to be created and in what style or tone.

Samples and Inspirations:
- http://scrollkin.example/
- http://zentrovo.example/#top
- http://brightmopservices.example/#about
- http://pixelgazette.example/inspiration/23-inspiring-single-page-designs
- http://www.tobiaskernstudio.example/
- http://www.ravelquist.example/

This I do not want:
- Too much popups (none if possible)
- Images of people
- Images of people in suits
- Stereotypical images of accountants
- Scrolling marquee
- Clip arts
Updates

Designers, I want to stress the fact that I am looking for a design, not simply a website. The website is 1 page long. Text and content should be minimal. So this means that the design has to do most of the talking. Please do not submit template like web designs, I can pull this off myself if needed. I need you to design a great header, footer and the connecting tissue from landing to end of the page. The entire design needs to flow.

Again, please do not use images of corp people or anything like that. Please think outside the box in how you want to express the company.

Some ideas:
An illustration from beginning to end of the website, have a story.
Add colors to the back ground. 
The background should not get in the way of reading the text, but it does not have to be boring.
Be bold in your design.

Also, please describe more about your design when you submit. Please don't submit a template like design and have no explanation for your actions.

Also, fee free to ask me questions. I am here to help. I check this everyday, so please contact if you need anything.

Designers, please read the details of my post before you submit the design.

If you have a great concept idea but is worry, you can go ahead and submit a pencil draft and ask my opinion before you work anymore on it.

Please see the website samples below for what I am really looking for:

Reason: Hi everyone, I am extending the deadline. It looks like some design are still pending completion, and I want you to have enough time to work on it.

Industry/Entity Type

Accounting

```html
<!DOCTYPE html>
<html lang="en">
<head>
<meta charset="utf-8">
<title>Lunar Ledger</title>
<link rel="stylesheet" href="https://fonts.googleapis.com/css2?family=Source+Sans+3:wght@300;400&display=swap">
<style>
  :root {
    --brand-blue: #2e3591;
    --brand-green: #96c93d;
    --ink: #333333;
    --nav-ink: #3a3a3a;
    --page: #ffffff;
    --rule: #e6e6e6;
    --art-light: #f4f4f4;
    --art-mid: #e4e4e4;
    --art-shade: #d2d2d2;
  }
  * { box-sizing: border-box; margin: 0; padding: 0; }
  html, body {
    width: 1200px;
    height: 820px;
    overflow: hidden;
    background: var(--page);
    font-family: "Source Sans 3", "Source Sans Pro", sans-serif;
  }
  .page {
    position: relative;
    width: 1200px;
    height: 820px;
    overflow: hidden;
  }
  .site-header {
    position: absolute;
    inset: 0 0 auto 0;
    height: 127px;
    background: var(--page);
    box-shadow: 0 1px 3px rgba(0, 0, 0, 0.12);
    z-index: 2;
  }
  .brand {
    position: absolute;
    left: 68px;
    top: 36px;
    font-size: 38px;
    font-weight: 400;
    letter-spacing: 2px;
    color: var(--brand-blue);
    text-decoration: none;
  }
  .main-nav {
    position: absolute;
    right: 49px;
    top: 47px;
    display: flex;
    gap: 38px;
  }
  .main-nav a {
    position: relative;
    font-size: 19px;
    color: var(--nav-ink);
    text-decoration: none;
  }
  .main-nav a.is-active { color: var(--brand-blue); }
  .main-nav a.is-active::after {
    content: "";
    position: absolute;
    left: 0;
    right: 0;
    bottom: -12px;
    height: 3px;
    background: var(--brand-blue);
  }
  .hero-title {
    position: absolute;
    left: 135px;
    top: 294px;
    font-size: 79px;
    font-weight: 300;
    line-height: 87px;
    color: var(--ink);
    letter-spacing: -0.5px;
  }
  .cta-button {
    position: absolute;
    left: 143px;
    top: 502px;
    width: 176px;
    height: 50px;
    border-radius: 8px;
    background: var(--brand-green);
    color: #fff;
    font-size: 25px;
    font-weight: 300;
    line-height: 50px;
    text-align: center;
    text-decoration: none;
  }
  .hero-art {
    position: absolute;
    left: 680px;
    top: 260px;
    width: 460px;
    height: 440px;
    background:
      radial-gradient(closest-side at 62% 80%, rgba(200,200,200,0.55) 0%, rgba(200,200,200,0) 100%),
      radial-gradient(closest-side at 50% 48%, var(--art-light) 0%, var(--art-mid) 55%, rgba(228,228,228,0) 100%);
  }
  .scroll-hint {
    position: absolute;
    right: 57px;
    top: 722px;
    display: flex;
    align-items: center;
    gap: 22px;
    color: var(--brand-green);
    font-size: 23px;
    font-weight: 300;
    text-decoration: none;
  }
  .section-rule {
    position: absolute;
    left: 0;
    right: 0;
    bottom: 0;
    height: 3px;
    background: var(--rule);
  }
</style>
</head>
<body>
<div class="page">
  <header class="site-header">
    <a class="brand" href="#home">lunarledger</a>
    <nav class="main-nav">
      <a class="is-active" href="#home">home</a>
      <a href="#services">products &amp; services</a>
      <a href="#clients">affiliates &amp; clients</a>
      <a href="#about">about</a>
      <a href="#contact">contact</a>
    </nav>
  </header>

  <section class="hero" id="home">
    <h1 class="hero-title">Fly, as we make it<br>hassle free.</h1>
    <a class="cta-button" href="#services">call to action</a>
    <div class="hero-art" role="img" aria-label="White folded paper plane gliding upward with a soft shadow"></div>
    <a class="scroll-hint" href="#services">
      <span>scroll down</span>
      <svg width="56" height="32" viewBox="0 0 56 32" aria-hidden="true">
        <polyline points="4,4 28,28 52,4" fill="none" stroke="#96c93d" stroke-width="7" stroke-linecap="round" stroke-linejoin="round"/>
      </svg>
    </a>
  </section>

  <div class="section-rule"></div>
</div>
</body>
</html>
```